Bright Ridge Electric Needs A Logo Design

We need a logo for my new company based out of Sacramento, Ca called Bright Ridge Electric. The name says it all, my electrical contracting business provides "Bright Ridge Professional Work" I'm open to any colors that pop and customers to say Wow. I would love to print my cards on metal.

Industry/Entity Type

Business

Contact Information for Business Card

The card needs to have as follows
Name of company: Bright Ridge Electric
My Name: Dorian Pelko
Phone # 916-382-5507
CL# 2087396
Email: brightridgeelectric@mailvance.net
and a slogan that represent "BRIGHT RIDGE"

Requirements
Must have
• The card needs to have as follows
• Name of company: Bright Ridge Electric
• My Name : Dorian Pelko
• Phone # 916-382-5507
• CL# 2087396
• Email: brightridgeelectric@mailvance.net
• and a slogan that represent "BRIGHT RIDGE"
Nice to have
• popping colors
• electrical Arcing

```html
<!DOCTYPE html>
<html lang="en">
<head>
<meta charset="utf-8">
<title>Bright Ridge Electric – Business Card</title>
<link rel="stylesheet" href="https://fonts.googleapis.com/css2?family=Play:wght@400;700&display=swap">
<style>
  :root {
    --page-bg: #ffffff;
    --card-black: #1c1c1c;
    --card-black-deep: #0f0f0f;
    --accent-yellow: #f7c515;
    --accent-orange: #f2920f;
    --steel-light: #d4d4d4;
    --steel-mid: #9a9a9a;
    --steel-dark: #5e5e5e;
    --text-white: #f1f1f1;
    --text-grey: #8c8c8c;
    --brand-silver: #e2e2e2;
  }
  * { margin: 0; padding: 0; box-sizing: border-box; }
  html, body {
    width: 1200px;
    height: 900px;
    overflow: hidden;
    background: var(--page-bg);
    font-family: "Play", sans-serif;
  }
  .business-card {
    position: absolute;
    left: 100px;
    top: 164px;
    width: 1000px;
    height: 572px;
    border-radius: 38px;
    overflow: hidden;
    background: radial-gradient(ellipse at 35% 40%, var(--card-black) 0%, var(--card-black-deep) 100%);
    box-shadow: 0 18px 40px rgba(0, 0, 0, 0.25);
  }
  .steel-panel {
    position: absolute;
    inset: 0;
    width: 100%;
    height: 100%;
  }
  .brand {
    position: absolute;
    left: 74px;
    top: 104px;
    display: flex;
    align-items: center;
    gap: 18px;
  }
  .brand-dot {
    width: 36px;
    height: 36px;
    border-radius: 50%;
    background: var(--accent-yellow);
    flex: none;
  }
  .brand-name {
    font-weight: 700;
    font-size: 58px;
    line-height: 1;
    letter-spacing: 1px;
    color: var(--brand-silver);
    white-space: nowrap;
  }
  .slogan {
    position: absolute;
    left: 130px;
    top: 184px;
    font-size: 22px;
    font-weight: 400;
    letter-spacing: 5px;
    text-transform: uppercase;
    color: var(--accent-yellow);
    white-space: nowrap;
  }
  .slogan-rule {
    position: absolute;
    left: 130px;
    top: 226px;
    width: 300px;
    height: 3px;
    background: linear-gradient(90deg, var(--accent-orange), transparent);
  }
  .holder-name {
    position: absolute;
    left: 70px;
    top: 330px;
    font-size: 34px;
    font-weight: 400;
    color: var(--accent-orange);
    letter-spacing: 0.5px;
  }
  .contact-list {
    position: absolute;
    left: 66px;
    top: 414px;
    list-style: none;
  }
  .contact-item {
    display: flex;
    align-items: center;
    gap: 8px;
    height: 44px;
    font-size: 30px;
    color: var(--text-white);
    white-space: nowrap;
  }
  .contact-icon {
    width: 34px;
    height: 34px;
    flex: none;
  }
  .licence {
    position: absolute;
    left: 110px;
    top: 508px;
    font-size: 22px;
    color: var(--text-grey);
    letter-spacing: 1px;
  }
</style>
</head>
<body>
  <section class="business-card">
    <svg class="steel-panel" viewBox="0 0 1000 572" aria-hidden="true">
      <defs>
        <linearGradient id="steel-sheen" x1="0" y1="0" x2="1" y2="1">
          <stop offset="0" stop-color="#9a9a9a"/>
          <stop offset="0.45" stop-color="#d4d4d4"/>
          <stop offset="0.75" stop-color="#9a9a9a"/>
          <stop offset="1" stop-color="#5e5e5e"/>
        </linearGradient>
      </defs>
      <polygon points="880,0 1000,0 1000,572 630,572" fill="#f2920f"/>
      <polygon points="900,0 1000,0 1000,572 652,572" fill="url(#steel-sheen)"/>
    </svg>

    <div class="brand">
      <span class="brand-dot"></span>
      <span class="brand-name">Bright Ridge Electric</span>
    </div>
    <p class="slogan">Bright Ridge Professional Work</p>
    <span class="slogan-rule"></span>

    <h1 class="holder-name">Dorian Pelko</h1>

    <ul class="contact-list">
      <li class="contact-item">
        <svg class="contact-icon" viewBox="0 0 34 34" aria-hidden="true">
          <circle cx="17" cy="17" r="15" fill="none" stroke="#f2920f" stroke-width="2.5"/>
          <path d="M11 9.5c1-.8 2.2-.6 2.8.4l1.6 2.7c.5.8.2 1.8-.5 2.3l-1 .7c.9 2 2.4 3.6 4.4 4.6l.7-1c.5-.8 1.5-1 2.3-.5l2.6 1.7c1 .6 1.1 1.9.3 2.8-1.2 1.3-3 1.8-4.7 1.1-4.5-1.8-8-5.4-9.6-10-.6-1.7-.1-3.6 1.1-4.8z" fill="#f7c515"/>
        </svg>
        <span>916-382-5507</span>
      </li>
      <li class="contact-item">
        <svg class="contact-icon" viewBox="0 0 34 34" aria-hidden="true">
          <circle cx="17" cy="17" r="15" fill="none" stroke="#f2920f" stroke-width="2.5"/>
          <rect x="9" y="11.5" width="16" height="11" rx="1" fill="#f7c515"/>
          <path d="M9.5 12l7.5 6 7.5-6" fill="none" stroke="#0f0f0f" stroke-width="1.4"/>
        </svg>
        <span>brightridgeelectric@mailvance.net</span>
      </li>
    </ul>

    <p class="licence">CL# 2087396</p>
  </section>
</body>
</html>
```